Using attached logo that has been created

Business card with logo that's attached. Maybe with water or the cartoon van in background. Looking for it to not be so plain and not too white.
Information to include;
Dario Whitlock
(555) 208-7713
Info@mossbrookpipeworks.example
www.mossbrookpipeworks.example
License # 5320417
Looking forward to the designs u come up with.
Thank you!
-Teresa
The designer (Brynn), that I would like to work with requested an extension to allow time to create a couple designs for this project.
Target Market(s)
Plumbing
Industry/Entity Type
Plumbing
Contact Information for Business Card
Listed above
Font styles to use
Look and feel

```html
<!DOCTYPE html>
<html lang="en">
<head>
<meta charset="utf-8">
<title>Mossbrook Pipeworks – Business Card</title>
<link href="https://fonts.googleapis.com/css2?family=Montserrat:wght@800&family=Roboto:wght@400;500;700&display=swap" rel="stylesheet">
<style>
  :root {
    --page: #e4e2e2;
    --blue-deep: #1558c4;
    --blue: #1f7fd0;
    --teal: #5cc3d1;
    --sky: #d7eef8;
    --navy: #0f3a8a;
    --yellow: #ffe31a;
    --white: #ffffff;
  }
  * { box-sizing: border-box; margin: 0; padding: 0; }
  html, body { width: 1200px; height: 973px; overflow: hidden; }
  body {
    background: var(--page);
    font-family: "Roboto", Arial, sans-serif;
    position: relative;
  }
  .card {
    position: absolute;
    top: 332px;
    width: 540px;
    height: 309px;
    overflow: hidden;
    box-shadow: 0 14px 30px rgba(0,0,0,.18);
  }
  .card--front { left: 40px; }
  .card--back { left: 620px; }

  .brand {
    position: absolute;
    font-family: "Montserrat", Arial, sans-serif;
    font-weight: 800;
    color: var(--navy);
    line-height: 1.1;
    text-transform: uppercase;
  }

  /* front */
  .front__bg {
    position: absolute; inset: 0;
    background: linear-gradient(160deg, var(--blue-deep) 0%, var(--blue) 55%, var(--teal) 100%);
  }
  .front__art { position: absolute; inset: 0; }
  .card--front .brand { left: 26px; top: 204px; font-size: 21px; width: 250px; }
  .contact-block { position: absolute; left: 292px; top: 58px; width: 240px; }
  .person-name {
    font-family: "Montserrat", Arial, sans-serif;
    font-weight: 800;
    font-size: 20px;
    color: var(--white);
    letter-spacing: .5px;
    text-transform: uppercase;
  }
  .person-name__last { color: var(--yellow); }
  .name-rule { width: 62px; height: 3px; background: var(--yellow); margin: 8px 0 26px; }
  .contact-list { list-style: none; }
  .contact-list li {
    display: flex; align-items: center; gap: 8px;
    font-size: 12.5px; margin-bottom: 9px; color: var(--white);
    white-space: nowrap;
  }
  .contact-list .is-yellow { color: var(--yellow); }
  .icon {
    flex: 0 0 16px; width: 16px; height: 16px; border-radius: 50%;
    background: var(--yellow); display: flex; align-items: center; justify-content: center;
  }
  .icon--light { background: var(--white); }
  .license { font-size: 10px; font-weight: 700; color: var(--white); margin-left: 24px; margin-top: -3px; }

  /* back */
  .back__bg { position: absolute; inset: 0; }
  .card--back .brand { left: 200px; top: 112px; font-size: 22px; width: 170px; }
  .back__web {
    position: absolute; left: 38px; top: 142px;
    font-size: 11px; color: var(--white);
    white-space: nowrap;
    transform: rotate(50deg); transform-origin: left top;
  }
</style>
</head>
<body>

<section class="card card--front" aria-label="Business card front">
  <div class="front__bg"></div>
  <svg class="front__art" width="540" height="309" viewBox="0 0 540 309">
    <defs>
      <linearGradient id="vanArea" x1="0" y1="0" x2="1" y2="1">
        <stop offset="0" stop-color="#eef1f5"/>
        <stop offset="1" stop-color="#dfe4ea"/>
      </linearGradient>
      <linearGradient id="mascot" x1="0" y1="0" x2="1" y2="1">
        <stop offset="0" stop-color="#9db4d6"/>
        <stop offset="1" stop-color="#8c7a5e"/>
      </linearGradient>
    </defs>
    <path d="M0 0 H290 C290 60 275 150 235 215 C200 265 130 285 0 290 Z" fill="url(#vanArea)" role="img" aria-label="Light service van illustration in the background"/>
    <rect x="140" y="22" width="120" height="168" rx="14" fill="url(#mascot)" opacity=".55" role="img" aria-label="Cartoon plumber mascot holding a pipe wrench and a saw"/>
  </svg>
  <div class="brand">Mossbrook Pipeworks &amp; More</div>

  <div class="contact-block">
    <div class="person-name">Dario <span class="person-name__last">Whitlock</span></div>
    <div class="name-rule"></div>
    <ul class="contact-list">
      <li class="is-yellow">
        <span class="icon"><svg width="9" height="9" viewBox="0 0 24 24"><path fill="#1558c4" d="M6.6 10.8a15 15 0 006.6 6.6l2.2-2.2a1 1 0 011-.25 11.4 11.4 0 003.6.57 1 1 0 011 1V20a1 1 0 01-1 1A17 17 0 013 4a1 1 0 011-1h3.5a1 1 0 011 1 11.4 11.4 0 00.57 3.6 1 1 0 01-.25 1z"/></svg></span>
        (555) 208-7713
      </li>
      <li>
        <span class="icon icon--light"><svg width="9" height="9" viewBox="0 0 24 24"><path fill="#1a1a1a" d="M2 5h20v14H2z M3 6l9 7 9-7" stroke="#fff" stroke-width="1.5"/></svg></span>
        Info@mossbrookpipeworks.example
      </li>
      <li class="is-yellow">
        <span class="icon"><svg width="9" height="9" viewBox="0 0 24 24"><path fill="#1a1a1a" d="M3 11l18-8-8 18-2-8z"/></svg></span>
        www.mossbrookpipeworks.example
      </li>
    </ul>
    <div class="license">License : #5320417</div>
  </div>
</section>

<section class="card card--back" aria-label="Business card back">
  <svg class="back__bg" width="540" height="309" viewBox="0 0 540 309">
    <defs>
      <linearGradient id="backBlue" x1="0" y1="0" x2="1" y2="1">
        <stop offset="0" stop-color="#1a63c9"/>
        <stop offset=".6" stop-color="#2a86d2"/>
        <stop offset="1" stop-color="#49b3d4"/>
      </linearGradient>
      <linearGradient id="backArt" x1="0" y1="0" x2="1" y2="1">
        <stop offset="0" stop-color="#6ea4dc"/>
        <stop offset="1" stop-color="#3f86cc"/>
      </linearGradient>
    </defs>
    <rect width="540" height="309" fill="url(#backBlue)"/>
    <rect x="340" y="40" width="170" height="200" rx="22" fill="url(#backArt)" opacity=".5" role="img" aria-label="Faint service van and cartoon plumber mascot illustration"/>
    <path d="M0 74 C70 120 150 200 210 309 H240 C180 195 100 110 0 60 Z" fill="var(--sky)"/>
    <path d="M0 74 C70 120 150 200 210 309 H0 Z" fill="#1a5fc6"/>
  </svg>
  <div class="back__web">www.mossbrookpipeworks.example</div>
  <div class="brand">Mossbrook Pipeworks &amp; More</div>
</section>

</body>
</html>
```